Business Card Design Coralgate Airflow Solutions

The Business will be centred around supply and installation of Ventilation for domestic homes and warehousing/workshops, and will be marketed as a Eco friendly means of reducing your carbon footprint and reducing energy consumption.Our suppliers will provide a range of products that will ventilate roof spaces and later will branch into to air transfer within homes for cooling and heating other rooms of the home etc.I would like to see colours that would be commensurate with the logo provided and yet not dominate the logo.Final design should convey a Diverse , professional but friendly service that will suit client needs

Target Market(s)

Domestic home owners and warehousing/workshop businesses

Industry/Entity Type

Business

Contact Information for Business Card

Company Name: Coralgate Airflow Solutions Pty Ltd, ABN: 42 817 359 264, Address: 27 Marrowfen Tulvanna W.A 6289, Email: dale@coralgateairflowsolutions.com.au, Mobile Number: 0461 852 309

Requirements
Nice to have
• A tract art that commensurate of the logo supplied
Should not have
• Font style that opposes logo design

```html
<!DOCTYPE html>
<html lang="en">
<head>
<meta charset="UTF-8">
<title>Coralgate Airflow Solutions – Business Card</title>
<link href="https://fonts.googleapis.com/css2?family=Arimo:wght@400;700&family=Michroma&display=swap" rel="stylesheet">
<style>
  :root {
    --stage: #2a2a2c;
    --green: #22b04b;
    --green-light: #43b860;
    --green-pale: #9fd6ae;
    --maroon: #5b2024;
    --paper: #f4f4f3;
    --paper-shade: #e4e4e3;
    --white: #ffffff;
  }
  * { box-sizing: border-box; margin: 0; padding: 0; }
  html, body {
    width: 1200px;
    height: 900px;
    overflow: hidden;
    background: var(--stage);
    font-family: "Arimo", Arial, sans-serif;
  }
  .sheet {
    width: 1200px;
    height: 900px;
    display: flex;
    flex-direction: column;
    align-items: center;
    justify-content: center;
    gap: 44px;
  }
  .card {
    width: 640px;
    height: 366px;
    border-radius: 18px;
    position: relative;
    overflow: hidden;
    box-shadow: 0 14px 30px rgba(0,0,0,0.45);
  }

  /* Front */
  .card--front {
    background: linear-gradient(120deg, var(--green-light) 0%, var(--green) 100%);
    color: var(--white);
  }
  .brand {
    position: absolute;
    left: 70px;
    top: 128px;
    display: flex;
    align-items: center;
    gap: 16px;
  }
  .brand__dot {
    width: 26px;
    height: 26px;
    border-radius: 50%;
    background: var(--white);
  }
  .brand__name {
    font-size: 36px;
    font-weight: 700;
    letter-spacing: 0.3px;
    color: var(--white);
  }
  .abn {
    position: absolute;
    right: 70px;
    top: 212px;
    font-size: 17px;
    letter-spacing: 0.5px;
  }

  /* Back */
  .card--back {
    background: linear-gradient(125deg, var(--white) 0%, var(--paper) 55%, var(--paper-shade) 100%);
    color: var(--maroon);
  }
  .back-brand {
    position: absolute;
    left: 34px;
    top: 44px;
    display: flex;
    align-items: center;
    gap: 10px;
  }
  .back-brand__dot {
    width: 16px;
    height: 16px;
    border-radius: 50%;
    background: var(--green);
  }
  .back-brand__name {
    font-size: 24px;
    font-weight: 700;
    color: var(--maroon);
  }
  .divider {
    position: absolute;
    left: 70px;
    top: 138px;
    width: 470px;
    height: 2px;
    background: linear-gradient(90deg, var(--green) 0%, var(--green) 40%, var(--maroon) 100%);
  }
  .person {
    position: absolute;
    left: 70px;
    top: 160px;
  }
  .person__name {
    font-family: "Michroma", "Arimo", sans-serif;
    font-size: 20px;
    color: var(--green);
    letter-spacing: 1px;
  }
  .person__title {
    font-size: 13px;
    color: var(--maroon);
    margin-left: 36px;
    margin-top: 2px;
  }
  .person__rule {
    width: 230px;
    height: 1px;
    background: var(--green-pale);
    margin-top: 6px;
  }
  .contacts {
    position: absolute;
    left: 70px;
    top: 232px;
    list-style: none;
    display: flex;
    flex-direction: column;
    gap: 9px;
  }
  .contacts__item {
    display: flex;
    align-items: center;
    gap: 12px;
    font-size: 14px;
    color: var(--maroon);
  }
  .contacts__icon {
    width: 18px;
    height: 18px;
    flex: none;
  }
</style>
</head>
<body>
<main class="sheet">

  <section class="card card--front" aria-label="Business card front">
    <div class="brand">
      <span class="brand__dot"></span>
      <span class="brand__name">Coralgate Airflow Solutions</span>
    </div>
    <p class="abn">ABN: 42 817 359 264</p>
  </section>

  <section class="card card--back" aria-label="Business card back">
    <div class="back-brand">
      <span class="back-brand__dot"></span>
      <span class="back-brand__name">Coralgate Airflow Solutions</span>
    </div>

    <div class="divider"></div>

    <div class="person">
      <p class="person__name">Name</p>
      <p class="person__title">Title</p>
      <div class="person__rule"></div>
    </div>

    <ul class="contacts">
      <li class="contacts__item">
        <svg class="contacts__icon" viewBox="0 0 18 18" aria-hidden="true">
          <rect x="4" y="1.5" width="10" height="15" rx="1.5" fill="none" stroke="#22b04b" stroke-width="1.6"/>
          <line x1="7.5" y1="13.5" x2="10.5" y2="13.5" stroke="#22b04b" stroke-width="1.4"/>
        </svg>
        <span>0461 852 309</span>
      </li>
      <li class="contacts__item">
        <svg class="contacts__icon" viewBox="0 0 18 18" aria-hidden="true">
          <rect x="1.5" y="4" width="15" height="10" fill="none" stroke="#22b04b" stroke-width="1.5"/>
          <polyline points="1.5,4 9,10 16.5,4" fill="none" stroke="#22b04b" stroke-width="1.5"/>
        </svg>
        <span>dale@coralgateairflowsolutions.com.au</span>
      </li>
      <li class="contacts__item">
        <svg class="contacts__icon" viewBox="0 0 18 18" aria-hidden="true">
          <circle cx="9" cy="9" r="7.5" fill="none" stroke="#22b04b" stroke-width="1.5"/>
          <ellipse cx="9" cy="9" rx="3.2" ry="7.5" fill="none" stroke="#22b04b" stroke-width="1.2"/>
          <line x1="1.5" y1="9" x2="16.5" y2="9" stroke="#22b04b" stroke-width="1.2"/>
        </svg>
        <span>www.coralgateairflowsolutions.com.au</span>
      </li>
      <li class="contacts__item">
        <svg class="contacts__icon" viewBox="0 0 18 18" aria-hidden="true">
          <path d="M9 17 C5 11.5 3.5 9 3.5 6.5 A5.5 5.5 0 0 1 14.5 6.5 C14.5 9 13 11.5 9 17 Z" fill="#22b04b"/>
          <circle cx="9" cy="6.5" r="2" fill="#ffffff"/>
        </svg>
        <span>27 Marrowfen Tulvanna W.A 6289</span>
      </li>
    </ul>
  </section>

</main>
</body>
</html>
```